Design Business Card Aerial Drone Photography

we need a business card that shows we are a leader in:
-Aerial Videos
-Aerial Photography
-Aerial Real Estate Photography
the attached logo is in blue, however please feel free to submit creative colors and designs
Updates

I would like to add the words "Veteran Owned and Operated" to my business card Certified Drone Operator should appear as one line Thanks, Ray Colton

Target Market(s)

real estate, cell towers, companies that want to showcase their company with aerial drone photography

Contact Information for Business Card

logo files have been submitted in pdf, jpg, png, .ai, .eps., .svg formats. Please feel free to be creative with design and colors, possibly a cloud type background
sample attached.
review my website www.bluefinskyworks.com that should help with designing my business card
Services:
-Aerial Videos
-Aerial Photography

Font styles to use
Sans Serif

Colors

Designer to choose colors to be used in the design.

Requirements
Must have
• company logo
• Bluefin Sky Works
• Ray Colton Certified Drone Operator
• 770-519-8462
• bluefinskyworks@mailbox.example
• www.bluefinskywarks.com
• 2716 Marlow Ln, Dunwoody GA 30338
Nice to have
• Please feel free to be creative with design and colors

```html
<!DOCTYPE html>
<html lang="en">
<head>
<meta charset="utf-8">
<title>Bluefin Sky Works – Business Card</title>
<link href="https://fonts.googleapis.com/css2?family=Lato:wght@400;700;900&display=swap" rel="stylesheet">
<style>
  :root{
    --brand-blue:#0b6fc3;
    --ink-grey:#5a5a5a;
    --band-grey:#8a8a8a;
    --paper:#ffffff;
    --backdrop:#e9ecef;
  }
  *{margin:0;padding:0;box-sizing:border-box}
  html,body{width:1200px;height:900px;overflow:hidden}
  body{background:var(--backdrop);font-family:'Lato',sans-serif;position:relative}
  .card{position:absolute;left:250px;width:700px;height:400px;overflow:hidden;
        box-shadow:0 6px 18px rgba(0,0,0,.15)}
  .card--back{top:40px;background:var(--brand-blue);color:var(--paper)}
  .card--front{top:470px;background:var(--paper)}

  /* back side */
  .brand-mark{position:absolute;left:56px;top:154px;display:flex;align-items:center;gap:12px}
  .brand-mark__dot{width:30px;height:30px;border-radius:50%;background:var(--paper);flex:none}
  .brand-mark__name{font-weight:900;font-size:22px;letter-spacing:.4px;text-transform:uppercase;color:var(--paper);white-space:nowrap}
  .services{position:absolute;left:370px;top:128px;list-style:none}
  .services li{font-weight:700;font-size:14px;text-transform:uppercase;margin-bottom:14px;
               padding-left:18px;position:relative;letter-spacing:.3px;white-space:nowrap}
  .services li::before{content:"";position:absolute;left:0;top:5px;width:7px;height:7px;
               border-radius:50%;background:var(--paper)}

  /* front side */
  .wave{position:absolute;left:0;top:0;width:700px;height:400px}
  .holder{position:absolute;left:50px;top:76px}
  .holder__name{font-weight:900;font-size:26px;color:var(--brand-blue);text-transform:uppercase;letter-spacing:.5px}
  .holder__title{font-size:19px;color:var(--ink-grey);margin-top:2px}
  .front-brand{position:absolute;right:46px;top:88px;display:flex;align-items:center;gap:10px}
  .front-brand__dot{width:22px;height:22px;border-radius:50%;background:var(--brand-blue)}
  .front-brand__name{font-weight:900;font-size:23px;color:var(--brand-blue);text-transform:uppercase;white-space:nowrap}
  .contact{position:absolute;left:50px;top:176px;list-style:none;color:var(--ink-grey)}
  .contact li{display:flex;align-items:center;gap:8px;font-size:18px;margin-bottom:6px;white-space:nowrap}
  .contact li.contact__address{margin-top:12px}
  .contact svg{width:17px;height:17px;fill:var(--brand-blue);flex:none}
  .website{position:absolute;right:30px;top:300px;color:var(--paper);font-size:17px;letter-spacing:.2px}
</style>
</head>
<body>

<section class="card card--back" aria-label="Card back">
  <div class="brand-mark">
    <span class="brand-mark__dot"></span>
    <span class="brand-mark__name">Bluefin Sky Works</span>
  </div>
  <ul class="services">
    <li>Aerial Videos</li>
    <li>Aerial Photography</li>
    <li>Aerial Real Estate Photography</li>
  </ul>
</section>

<section class="card card--front" aria-label="Card front">
  <svg class="wave" viewBox="0 0 700 400" aria-hidden="true">
    <path d="M0 318 C150 358 320 348 450 268 C560 200 630 184 700 188 L700 204 C630 200 560 216 450 286 C320 366 150 376 0 346 Z" fill="var(--band-grey)"/>
    <path d="M0 356 C150 386 320 376 450 296 C560 226 630 210 700 214 L700 400 L0 400 Z" fill="var(--brand-blue)"/>
  </svg>

  <div class="holder">
    <h1 class="holder__name">Ray Colton</h1>
    <p class="holder__title">Certified Drone Operator</p>
  </div>

  <div class="front-brand">
    <span class="front-brand__dot"></span>
    <span class="front-brand__name">Bluefin Sky Works</span>
  </div>

  <ul class="contact">
    <li>
      <svg viewBox="0 0 24 24" aria-hidden="true"><path d="M6.6 10.8a15.1 15.1 0 0 0 6.6 6.6l2.2-2.2c.3-.3.7-.4 1-.2 1.1.4 2.3.6 3.6.6.6 0 1 .4 1 1V20c0 .6-.4 1-1 1A17 17 0 0 1 3 4c0-.6.4-1 1-1h3.5c.6 0 1 .4 1 1 0 1.3.2 2.5.6 3.6.1.3 0 .7-.2 1z"/></svg>
      770-519-8462
    </li>
    <li>
      <svg viewBox="0 0 24 24" aria-hidden="true"><path d="M2 5h20v14H2z M4 7v.5l8 5 8-5V7l-8 5z" fill-rule="evenodd"/></svg>
      bluefinskyworks@mailbox.example
    </li>
    <li class="contact__address">2716 Marlow Ln, Dunwoody GA 30338</li>
  </ul>

  <p class="website">www.bluefinskyworks.com</p>
</section>

</body>
</html>
```